New bussiness card, using company logo.
Gerald Finch
Manager/Director
Finch Property Developments
Po Box 4637
Thuringowa Central
Qld
0412 558 306
gerald@finchpropertydevelopments
eye catching, vibrant colours, professional

It Company

```html
<!DOCTYPE html>
<html lang="en">
<head>
<meta charset="utf-8">
<title>Finch Property Developments – Business Card</title>
<link rel="stylesheet" href="https://fonts.googleapis.com/css2?family=Arimo:wght@400;700&family=Roboto+Condensed:wght@700&display=swap">
<style>
  :root {
    --green: #a9cf46;
    --green-soft: #d3e8a0;
    --cream: #fefdf2;
    --ink: #1f1f1f;
    --edge: #e3e3e3;
    --white: #ffffff;
    --page: #ffffff;
  }
  * { margin: 0; padding: 0; box-sizing: border-box; }
  html, body {
    width: 1200px;
    height: 1000px;
    overflow: hidden;
    background: var(--page);
  }
  .canvas {
    position: relative;
    width: 1200px;
    height: 1000px;
    font-family: "Arimo", Arial, sans-serif;
    color: var(--ink);
  }
  .card {
    position: absolute;
    left: 218px;
    width: 766px;
    height: 469px;
    background: var(--cream);
    border: 1px solid var(--edge);
    overflow: hidden;
  }
  .card--front { top: 25px; }
  .card--back { top: 507px; }

  .brand-panel {
    position: absolute;
    left: 0;
    top: 0;
    width: 320px;
    height: 100%;
    background: var(--green);
  }
  .brand-name {
    position: absolute;
    left: 25px;
    top: 208px;
    width: 270px;
    font-weight: 700;
    font-size: 25px;
    line-height: 30px;
    letter-spacing: 0.5px;
    text-transform: uppercase;
    color: var(--white);
  }

  .contact-name {
    position: absolute;
    right: 25px;
    top: 210px;
    font-family: "Roboto Condensed", "Arial Narrow", sans-serif;
    font-weight: 700;
    font-size: 21px;
    letter-spacing: 1px;
    text-align: right;
  }
  .contact-role {
    position: absolute;
    right: 25px;
    top: 236px;
    font-size: 20px;
    letter-spacing: 0.8px;
    text-align: right;
  }
  .contact-details {
    position: absolute;
    right: 25px;
    top: 361px;
    font-size: 20px;
    line-height: 22.5px;
    letter-spacing: 0.9px;
    text-align: right;
    font-style: normal;
    white-space: nowrap;
  }

  .roofline-art {
    position: absolute;
    left: 102px;
    top: 196px;
    width: 560px;
    height: 96px;
    background: linear-gradient(to bottom, var(--cream), var(--green-soft));
  }
  .back-band {
    position: absolute;
    left: 0;
    top: 291px;
    width: 100%;
    height: 178px;
    background: var(--green);
  }
  .back-company {
    position: absolute;
    left: 0;
    top: 361px;
    width: 100%;
    text-align: center;
    font-size: 31px;
    letter-spacing: 1.5px;
    text-transform: uppercase;
    color: var(--ink);
  }
</style>
</head>
<body>
<main class="canvas">
  <section class="card card--front" aria-label="Business card front">
    <div class="brand-panel">
      <div class="brand-name">Finch Property Developments</div>
    </div>
    <h1 class="contact-name">Gerald Finch</h1>
    <p class="contact-role">Manager/Director</p>
    <address class="contact-details">
      Po Box 4637,<br>
      Thuringowa Central<br>
      Qld 0412 558 306<br>
      gerald@finchpropertydevelopments
    </address>
  </section>

  <section class="card card--back" aria-label="Business card back">
    <div class="roofline-art" role="img" aria-label="Green roofline decoration of three house gables resting on the band"></div>
    <div class="back-band"></div>
    <p class="back-company">Finch Property Developments</p>
  </section>
</main>
</body>
</html>
```